TVQ-Business Card Design

I need a modern, professional business card design that includes my logo as the main feature, maybe the entire background with the contact info overlaying or even contact info on the back and the logo full frontal

Neat and organized placement of contact information

Would like to see options in black and white

Target Market(s)

real estate Developers, Construction managers, business and home owners

Industry/Entity Type

Construction

Contact Information for Business Card

TVQ Construction
Dennis Fairweather
General Contractor

Office: 1-888-902-7351 Ext #1
Cell: 412-730-2168
Fax: 1-888-902-7351

Font styles to use
Serif

Requirements
Must have
• title
• office #
• cell #
• Email
• website
Nice to have
• fax

```html
<!DOCTYPE html>
<html lang="en">
<head>
<meta charset="utf-8">
<title>TVQ Construction – Business Cards</title>
<link rel="stylesheet" href="https://fonts.googleapis.com/css2?family=Arimo:wght@400;700&display=swap">
<style>
  :root {
    --backdrop: #2e2a27;
    --card: #141414;
    --card-edge: #1f1f1f;
    --green: #2aa84a;
    --green-dark: #1d7a35;
    --silver: #a9a9a9;
    --text: #f2f2f2;
    --divider: #5a5a5a;
  }
  * { box-sizing: border-box; margin: 0; padding: 0; }
  html, body {
    width: 1200px; height: 787px; overflow: hidden;
    background: var(--backdrop);
    font-family: "Arimo", Arial, sans-serif;
  }
  .stage {
    width: 1200px; height: 787px;
    display: flex; align-items: center; justify-content: center; gap: 60px;
  }
  .card {
    width: 525px; height: 300px;
    background: var(--card);
    border: 1px solid var(--card-edge);
    box-shadow: 0 10px 30px rgba(0,0,0,.45);
    position: relative;
  }
  /* Back: brand face */
  .card--brand {
    display: flex; flex-direction: column; align-items: center; justify-content: center; gap: 28px;
  }
  .brand-mark {
    display: flex; align-items: center; gap: 16px;
    color: var(--silver); font-weight: 700;
  }
  .brand-mark__square { width: 26px; height: 26px; background: var(--silver); }
  .brand-mark__name { font-size: 46px; letter-spacing: 1px; }
  .brand-url {
    color: var(--silver); font-size: 15px; letter-spacing: 5px;
  }
  /* Front: contact face */
  .card--contact { display: flex; align-items: center; padding: 0 30px; }
  .contact-brand {
    width: 210px; display: flex; align-items: center; gap: 10px;
    color: var(--green); font-weight: 700;
  }
  .contact-brand__square { width: 16px; height: 16px; background: var(--green); flex: none; }
  .contact-brand__name { font-size: 24px; line-height: 1.1; }
  .contact-divider { width: 1px; height: 170px; background: var(--divider); margin: 0 22px; }
  .contact-info { color: var(--text); }
  .person-name { color: var(--green); font-size: 19px; font-weight: 700; }
  .person-title { font-size: 15px; margin-bottom: 14px; }
  .contact-list { list-style: none; }
  .contact-list li {
    display: flex; align-items: center; gap: 10px;
    font-size: 14px; line-height: 22px;
  }
  .contact-list svg { width: 13px; height: 13px; fill: var(--green); flex: none; }
</style>
</head>
<body>
<main class="stage">
  <section class="card card--brand" aria-label="Card back">
    <div class="brand-mark">
      <span class="brand-mark__square"></span>
      <span class="brand-mark__name">TVQ Construction</span>
    </div>
    <p class="brand-url">www.website.com</p>
  </section>

  <section class="card card--contact" aria-label="Card front">
    <div class="contact-brand">
      <span class="contact-brand__square"></span>
      <span class="contact-brand__name">TVQ Construction</span>
    </div>
    <div class="contact-divider"></div>
    <div class="contact-info">
      <p class="person-name">Dennis Fairweather</p>
      <p class="person-title">General Contractor</p>
      <ul class="contact-list">
        <li><svg viewBox="0 0 16 16"><path d="M3 1h3l1 4-2 1c1 2 3 4 5 5l1-2 4 1v3c0 1-1 2-2 2C7 15 1 9 1 3c0-1 1-2 2-2z"/></svg>1-888-902-7351 Ext #1</li>
        <li><svg viewBox="0 0 16 16"><path d="M4 0h8a1 1 0 0 1 1 1v14a1 1 0 0 1-1 1H4a1 1 0 0 1-1-1V1a1 1 0 0 1 1-1zm1 2v10h6V2z"/></svg>412-730-2168</li>
        <li><svg viewBox="0 0 16 16"><path d="M4 0h7v4H4zM1 5h14v8h-3v3H4v-3H1zm5 7v2h4v-2z"/></svg>1-888-902-7351</li>
        <li><svg viewBox="0 0 16 16"><path d="M0 3h16v10H0zm1 1v1l7 5 7-5V4z"/></svg>name@website.com</li>
        <li><svg viewBox="0 0 16 16"><circle cx="8" cy="8" r="7"/></svg>www.website.com</li>
      </ul>
    </div>
  </section>
</main>
</body>
</html>
```